Touring Cabaret Seasons Needs a Poster Design

We need a poster design for upcoming Cabaret seasons in Melbourne and Adelaide (Australia) for a prestigious festival.

Show is titled "Hold Still While I Tune My Ukulele..." and is a comedy parody of bad cabaret and deluded performers. We'd like the poster to reflect the comedy of the piece without being silly and inaccessable.

Artist has recently won awards for this show and these will need to be listed as a part of the design.

I have attached a couple of photographs that can be used - one is the artist with a blank book cover and these could be used to overlay text.

Would like it to not look too wordy, however I realise we've asked for a lot of text to be included.

Target Market(s)

Ages 20 - 40 cabaret or comedy fans.

Industry/Entity Type

Festival

Requirements
Must have
• TEXT:
The Velvet Lantern presents:
Hold Still While I Tune My Ukulele...

TEXT:
WINNER of BEST CABARET, BEST WRITING and PEOPLE’S CHOICE awards at Brisk + Bright Revue 2011

TEXT:
The Copper Kettle (Melbourne)
Feb 23rd to the 26th

El Faro, REVedge(Adelaide)
March 3rd and 4th

QUOTES:
“...the funniest things in spandex. 4.5 stars” – The Ledger on Dribble! A revue about handball.

“a clever dissection of bad cabaret” – Owen Marsh, The Ledger on Brisk + Bright Revue
Nice to have
• TEXT:
The last time someone showed you a little something they were working on, did you lose an hour of your life you will never get back? Don’t worry – we’ve all been there.

TEXT:
Composer and co-writer of Dribble! (A revue about handball) and WINNER of BEST CABARET, BEST WRITING and PEOPLE’S CHOICE awards at Brisk + Bright Revue 2011, presents her full show, with more original music and helpful anecdotes.

WEBSITE:
More info at www.pagebook.example/thevelvetlantern

```html
<!DOCTYPE html>
<html lang="en">
<head>
<meta charset="utf-8">
<title>The Velvet Lantern presents: Hold Still While I Tune My Ukulele...</title>
<link rel="stylesheet" href="https://fonts.googleapis.com/css2?family=Oswald:wght@500&family=Quantico:wght@400;700&family=Ubuntu:wght@500&display=swap">
<style>
  :root {
    --mat: #ffffff;
    --frame: #000000;
    --stage-dark: #0b0504;
    --stage-warm: #3a1a0c;
    --stage-glow: #5a2a12;
    --tan: #b08a5e;
    --gold: #f2c873;
    --quote: #e6c47a;
    --title: #ffffff;
    --band: #7a2a14;
    --band-ink: #2b0d06;
  }
  * { margin: 0; padding: 0; box-sizing: border-box; }
  html, body { width: 1200px; height: 1200px; overflow: hidden; background: var(--mat); }
  .mount {
    position: relative; width: 1200px; height: 1200px;
    background: var(--mat); border: 14px solid var(--frame);
  }
  .poster {
    position: absolute; left: 206px; top: 48px;
    width: 768px; height: 1078px; overflow: hidden;
    background: var(--stage-dark);
  }
  .stage-photo {
    position: absolute; inset: 0 0 134px 0;
    background:
      radial-gradient(ellipse 45% 40% at 60% 70%, var(--stage-glow) 0%, transparent 70%),
      radial-gradient(ellipse 30% 35% at 95% 55%, #4a2010 0%, transparent 70%),
      radial-gradient(ellipse 25% 20% at 20% 58%, #24100a 0%, transparent 80%),
      linear-gradient(180deg, #130806 0%, var(--stage-warm) 55%, #1a0a06 100%);
  }
  .company {
    position: absolute; left: 35px; top: 50px; width: 698px;
    font-family: "Quantico", sans-serif; font-weight: 700;
    font-size: 46px; letter-spacing: 3px; color: var(--tan);
    text-align: center; line-height: 1;
  }
  .venue {
    position: absolute; top: 132px;
    font-family: "Quantico", sans-serif; font-weight: 700;
    font-size: 16px; line-height: 17px; color: var(--tan); text-transform: uppercase;
  }
  .venue .dates { color: var(--gold); margin-top: 10px; font-size: 17px; }
  .venue--melbourne { left: 42px; }
  .venue--adelaide { right: 40px; text-align: right; }
  .presents {
    position: absolute; left: 262px; top: 126px; width: 244px; text-align: center;
    font-family: "Quantico", sans-serif; font-weight: 700;
    font-size: 56px; line-height: 1; color: var(--tan); letter-spacing: 1px;
  }
  .show-title {
    position: absolute; left: 44px; top: 270px;
    font-family: "Oswald", sans-serif; font-weight: 500; color: var(--title);
    text-transform: uppercase; line-height: 1;
  }
  .show-title .line-1 { display: block; font-size: 92px; letter-spacing: 1px; }
  .show-title .small { font-size: 56px; vertical-align: 18px; }
  .show-title .line-2 { display: block; font-size: 74px; margin-top: 6px; }
  .accolades {
    position: absolute; left: 44px; top: 728px; width: 420px;
    font-family: "Quantico", sans-serif; font-weight: 700;
    font-size: 15px; line-height: 18px; color: var(--quote); text-transform: uppercase;
  }
  .accolades blockquote { margin-bottom: 26px; }
  .accolades .plain-case { text-transform: none; }
  .blurb {
    position: absolute; left: 0; bottom: 0; width: 768px; height: 134px;
    background: var(--band); padding: 14px 30px 0 36px;
    font-family: "Ubuntu", sans-serif; font-weight: 500;
    font-size: 13.5px; line-height: 20px; color: var(--band-ink);
  }
  .blurb p + p { margin-top: 14px; }
</style>
</head>
<body>
<div class="mount">
  <article class="poster">
    <div class="stage-photo" role="img" aria-label="Stage photograph: a pianist at a grand piano on the left, the singer in a black strapless gown and gold gloves reaching out centre stage, a second performer in the background, warm stage lights above"></div>

    <h2 class="company">THE VELVET LANTERN</h2>
    <div class="venue venue--melbourne">
      <p>The Copper Kettle<br>(Melbourne)</p>
      <p class="dates">Feb 23rd to the 26th</p>
    </div>
    <p class="presents">PRESENTS:</p>
    <div class="venue venue--adelaide">
      <p>El Faro,<br>REVedge(Adelaide)</p>
      <p class="dates">March 3rd and 4th</p>
    </div>

    <h1 class="show-title">
      <span class="line-1">Hold Still <span class="small">While</span> I Tune</span>
      <span class="line-2">My Ukulele...</span>
    </h1>

    <div class="accolades">
      <blockquote>“Winner of Best Cabaret, Best Writing and People’s Choice awards at Brisk + Bright Revue 2011“</blockquote>
      <blockquote>“...The funniest things in spandex. 4.5 stars”<br>- The Ledger on Dribble! A revue about handball.</blockquote>
      <blockquote>“A clever dissection of bad cabaret”<br><span class="plain-case">- Owen Marsh, The Ledger on Brisk + Bright Revue</span></blockquote>
    </div>

    <footer class="blurb">
      <p>The last time someone showed you a little something they were working on, did you lose an hour of your life you will never get back? Don't worry - we've all been there.</p>
      <p>Composer and co-writer of Dribble! (A revue about handball) and WINNER of BEST CABARET, BEST WRITING and PEOPLE'S CHOICE awards at Brisk + Bright Revue 2011, presents her full show, with more original music and helpful anecdote</p>
    </footer>
  </article>
</div>
</body>
</html>
```